Restaurant needs promotional material

We need a design for a "free welcome cocktail on your next visit" flyer. The flyer must have a black background and be contemporary. Our logo is the name of the restaurant which is "Amber Nook" in edwardian script font with italic selected.

There must be a section for terms and conditions, which are:
1 free cocktail for every main course ordered from our evening menu over the value of 9.95€ (not including taxes). The number of free cocktails cannot exceed the number of main courses ordered from your previous visit. This offer is only valid when you present both this flyer and your receipt from your previous visit. This offer does not include ice cream cocktails. This offer cannot be used in conjunction with any other offer or promotion. Limit 1 free cocktail per person. We reserve the right to final interpretation of this offer and can cancel the offer at any time.

A space must also be left where we can write a "valid until" date.

The uploaded photos are a picture of our cocktail menu and the publicity we are currently running, so you can get a feel for your design.

Thanks

Industry/Entity Type

Restaurant

Colors
000000

Requirements
Must have
• Also included in the flyer is the text " Please present this flyer along with your bill from your previous visit upon arrival.
• Pictures of cocktails!

```html
<!DOCTYPE html>
<html lang="en">
<head>
<meta charset="utf-8">
<title>Amber Nook – Free Welcome Cocktail Flyer</title>
<link rel="stylesheet" href="https://fonts.googleapis.com/css2?family=Archivo:wght@700;800&family=Arimo:wght@400&display=swap">
<style>
  :root {
    --page: #ffffff;
    --ink: #000000;
    --brand-red: #ec1c35;
    --glow-rust: #7a3324;
    --glow-wine: #6e2320;
    --glow-brown: #5a3020;
    --text-light: #ffffff;
    --text-soft: #e6e6e6;
    --field: #8c7068;
    --art-red: #d92a3a;
    --art-amber: #f0b41c;
    --art-sky: #5cc4e4;
  }
  * { margin: 0; padding: 0; box-sizing: border-box; }
  html, body {
    width: 1200px;
    height: 1200px;
    overflow: hidden;
    background: var(--page);
  }
  .canvas {
    position: relative;
    width: 1200px;
    height: 1200px;
  }
  .flyer {
    position: absolute;
    left: 50px;
    top: 341px;
    width: 1100px;
    height: 518px;
    overflow: hidden;
    color: var(--text-light);
    font-family: "Arimo", Arial, sans-serif;
    background:
      radial-gradient(ellipse 260px 220px at 330px 40px, rgba(122,51,36,0.85), transparent 70%),
      radial-gradient(ellipse 420px 160px at 820px 10px, rgba(110,55,35,0.75), transparent 75%),
      radial-gradient(ellipse 120px 300px at 10px 330px, rgba(110,35,32,0.8), transparent 75%),
      radial-gradient(ellipse 360px 140px at 300px 520px, rgba(90,40,28,0.6), transparent 75%),
      radial-gradient(ellipse 300px 260px at 1100px 300px, rgba(90,48,32,0.55), transparent 75%),
      var(--ink);
  }
  .brand-block {
    position: absolute;
    left: 57px;
    top: 0;
    width: 252px;
    height: 284px;
    background: var(--brand-red);
    display: flex;
    align-items: center;
    justify-content: center;
  }
  .brand-name {
    font-family: "Archivo", Arial, sans-serif;
    font-weight: 700;
    font-size: 42px;
    line-height: 1.05;
    color: var(--text-light);
    text-align: center;
  }
  .headline {
    position: absolute;
    left: 334px;
    top: 72px;
    font-family: "Archivo", Arial, sans-serif;
    font-weight: 800;
    color: var(--text-light);
  }
  .headline-free { display: block; font-size: 64px; line-height: 62px; }
  .headline-offer { display: block; font-size: 51px; line-height: 52px; }
  .headline-visit { display: block; font-size: 34px; line-height: 38px; font-weight: 700; }
  .valid-until {
    position: absolute;
    left: 878px;
    top: 64px;
    font-size: 12px;
    letter-spacing: 0.2px;
    color: var(--text-soft);
  }
  .valid-field {
    position: absolute;
    left: 878px;
    top: 81px;
    width: 222px;
    height: 40px;
    background: var(--field);
  }
  .cocktail-art {
    position: absolute;
    left: 644px;
    top: 208px;
    width: 390px;
    height: 232px;
    border-radius: 10px;
    background:
      radial-gradient(circle at 18% 30%, rgba(217,42,58,0.55), transparent 38%),
      radial-gradient(circle at 52% 45%, rgba(240,180,28,0.5), transparent 38%),
      radial-gradient(circle at 84% 38%, rgba(92,196,228,0.5), transparent 36%),
      #111111;
  }
  .terms-label {
    position: absolute;
    left: 50px;
    top: 341px;
    height: 122px;
    writing-mode: vertical-rl;
    transform: rotate(180deg);
    font-size: 11.5px;
    color: var(--text-soft);
    text-align: center;
  }
  .terms-rule {
    position: absolute;
    left: 70px;
    top: 343px;
    width: 1px;
    height: 118px;
    background: var(--text-soft);
    opacity: 0.6;
  }
  .terms-list {
    position: absolute;
    left: 78px;
    top: 335px;
    width: 590px;
    list-style: none;
    font-size: 11.6px;
    line-height: 14.9px;
    color: var(--text-soft);
  }
  .terms-list li {
    position: relative;
    padding-left: 15px;
  }
  .terms-list li::before {
    content: "";
    position: absolute;
    left: 0;
    top: 4px;
    width: 6px;
    height: 6px;
    background: var(--text-soft);
  }
</style>
</head>
<body>
  <main class="canvas">
    <section class="flyer">
      <div class="brand-block">
        <span class="brand-name">Amber<br>Nook</span>
      </div>

      <h1 class="headline">
        <span class="headline-free">FREE !</span>
        <span class="headline-offer">welcome cocktail</span>
        <span class="headline-visit">on your next visit *</span>
      </h1>

      <p class="valid-until">VALID UNTIL :</p>
      <div class="valid-field"></div>

      <div class="cocktail-art" role="img" aria-label="Illustration of three cocktails: a red margarita with a cherry and umbrella, an orange hurricane glass with a lemon slice, and a blue martini with a straw"></div>

      <p class="terms-label">* Terms &amp; Conditions</p>
      <div class="terms-rule"></div>
      <ul class="terms-list">
        <li>1 free cocktail for every main course ordered from our evening menu over the value of 9.95 €<br>(not including taxes).</li>
        <li>The number of free cocktails cannot exceed the number of main courses ordered from your previous visit.</li>
        <li>This offer is only valid when you present both this flyer and your receipt from your previous visit.</li>
        <li>This offer does not include ice cream cocktails. This offer cannot be used in conjunction with any other<br>offer or promotion.</li>
        <li>Limit 1 free cocktail per person.</li>
        <li>We reserve the right to final interpretation of this offer and can cancel the offer at any time.</li>
      </ul>
    </section>
  </main>
</body>
</html>
```